Instagram adverts for international jewellery making school

We need 10 single image Instagram adverts to promote our jewellery school in Kuala Lumpur Malaysia to an international market. The images should all have a different feel and it is up to the designer to also come up with wording to include on the images - you can refer to our website for details on the classes https://maradenholtcraft.com/starter-2. <br/><br/>The feeling and wording should be fun, vibrant and quirky - no need to be too serious here, and I generally prefer busier images - they won't be used for promotional posts so no need to worry about Instagram / FB ad restrictions<br/><br/>We have attached an example of one Instagram ad we created ourselves for reference.<br/><br/>We only need to see one advert before selecting you as a designer and we are looking to build an ongoing relationship for all future graphic design needs. <br/><br/>We will send a google drive of images to the chosen designer but for now, please just use the images from the website for the prototype.

Font styles to use
Serif
Sans Serif

Colors

Designer to choose colors to be used in the design.

Requirements
Must have
• Fun bold vibrant feel
Nice to have
• Multiple images included in each post

```html
<!DOCTYPE html>
<html lang="en">
<head>
<meta charset="utf-8">
<title>Mara Denholt Craft – A little Creativity</title>
<link href="https://fonts.googleapis.com/css2?family=Great+Vibes&family=Montserrat:wght@500;600&display=swap" rel="stylesheet">
<style>
  :root {
    --paper: #eeeae3;
    --paper-tint: #e3d9e2;
    --gem-tint: #cdb3c8;
    --pink-left: #ee82cf;
    --pink-right: #f45d7e;
    --pink-hot: #f0609a;
    --magenta: #e370d2;
    --white: #ffffff;
    --line-pink: #f0508a;
  }
  * { margin: 0; padding: 0; box-sizing: border-box; }
  html, body { width: 1200px; height: 1200px; overflow: hidden; background: var(--paper); }
  .ad {
    position: relative;
    width: 1200px;
    height: 1200px;
    overflow: hidden;
  }
  .ad__photo {
    position: absolute;
    inset: 0;
    background:
      radial-gradient(circle at 25% 30%, var(--gem-tint) 0%, transparent 35%),
      radial-gradient(circle at 80% 75%, var(--gem-tint) 0%, transparent 30%),
      radial-gradient(circle at 70% 20%, var(--paper-tint) 0%, transparent 40%),
      linear-gradient(135deg, var(--paper) 0%, var(--paper-tint) 100%);
  }
  .ad__shapes {
    position: absolute;
    inset: 0;
    width: 1200px;
    height: 1200px;
  }
  .headline {
    position: absolute;
    left: 0;
    width: 1200px;
    text-align: center;
    color: var(--white);
    font-family: "Montserrat", sans-serif;
  }
  .headline__lead {
    top: 432px;
    left: -8px;
    font-size: 33px;
    font-weight: 600;
  }
  .headline__script {
    top: 468px;
    left: 10px;
    font-family: "Great Vibes", cursive;
    font-size: 128px;
    font-weight: 400;
    line-height: 1;
  }
  .headline__sub {
    top: 637px;
    left: 10px;
    font-size: 25px;
    font-weight: 500;
  }
  .headline__strong {
    top: 685px;
    left: 10px;
    font-size: 38px;
    font-weight: 600;
    letter-spacing: 0.5px;
  }
  .brand {
    position: absolute;
    right: 32px;
    bottom: 40px;
    width: 200px;
    text-align: center;
    color: var(--white);
    font-family: "Montserrat", sans-serif;
    font-weight: 500;
  }
  .brand__mark {
    width: 70px;
    height: 70px;
    margin: 0 auto 12px;
    border: 2px solid var(--white);
    border-radius: 50%;
  }
  .brand__name { font-size: 19px; letter-spacing: 1.5px; line-height: 1.2; }
  .brand__tag { font-size: 15px; letter-spacing: 1px; }
</style>
</head>
<body>
<main class="ad">
  <div class="ad__photo" role="img" aria-label="Photo of hand-drawn jewellery design sketches with loose pink, green and purple cabochon gemstones"></div>

  <svg class="ad__shapes" viewBox="0 0 1080 1080" aria-hidden="true">
    <defs>
      <linearGradient id="centre-blob" x1="0" y1="0" x2="1" y2="0.4">
        <stop offset="0" stop-color="var(--pink-left)"/>
        <stop offset="1" stop-color="var(--pink-right)"/>
      </linearGradient>
      <linearGradient id="corner-blob-top" x1="0" y1="0" x2="1" y2="0">
        <stop offset="0" stop-color="var(--magenta)"/>
        <stop offset="1" stop-color="var(--pink-hot)"/>
      </linearGradient>
      <linearGradient id="corner-blob-bottom" x1="0" y1="0" x2="1" y2="1">
        <stop offset="0" stop-color="var(--magenta)"/>
        <stop offset="1" stop-color="var(--pink-hot)"/>
      </linearGradient>
    </defs>

    <path class="blob blob--top-left" fill="url(#corner-blob-top)" opacity="0.95"
      d="M0,0 H360 C380,60 330,110 260,130 C190,150 170,220 110,240 C60,255 20,230 0,252 Z"/>
    <path class="blob blob--bottom-right" fill="url(#corner-blob-bottom)" opacity="0.95"
      d="M1080,770 C1000,760 960,820 900,860 C840,900 760,880 700,930 C650,970 630,1040 640,1080 H1080 Z"/>
    <path class="blob blob--centre" fill="url(#centre-blob)" opacity="0.92"
      d="M330,300 C380,230 470,250 520,215 C600,165 700,200 720,280 C740,340 830,310 880,380 C930,450 920,560 890,640 C860,710 780,690 720,730 C660,770 620,810 540,780 C460,750 380,770 310,750 C240,730 200,650 215,560 C230,470 270,380 330,300 Z"/>

    <g class="orbit-lines" fill="none" stroke="var(--line-pink)" stroke-width="1.5">
      <path d="M250,340 C420,300 700,300 830,330 C930,355 930,430 880,470"/>
      <path d="M500,735 C600,800 720,790 770,740 C800,705 790,640 760,600"/>
    </g>

    <g class="sparkles" fill="none" stroke="var(--white)" stroke-width="3" stroke-linecap="round">
      <path d="M262,320 L298,356 M298,320 L262,356"/>
      <path d="M318,722 V758 M300,740 H336"/>
      <circle cx="640" cy="355" r="28"/>
      <circle cx="775" cy="812" r="28"/>
    </g>
    <g class="dots" fill="var(--white)">
      <circle cx="196" cy="548" r="38"/>
      <circle cx="845" cy="562" r="18"/>
    </g>
  </svg>

  <p class="headline headline__lead">A little</p>
  <h1 class="headline headline__script">Creativity!</h1>
  <p class="headline headline__sub">is all you need to become a</p>
  <p class="headline headline__strong">JEWELLERY DESIGNER!</p>

  <div class="brand">
    <div class="brand__mark"></div>
    <p class="brand__name">MARA DENHOLT</p>
    <p class="brand__tag">craft</p>
  </div>
</main>
</body>
</html>
```